Water Delivery Service Website

We are working with BrivoNeté. They are a water delivery company and in need of a new website design.
Some sites to use for inspiration:
https://www.corvindale.example/home
https://www.plumtidego.example/en/home3
https://www.zelkop.example
https://www.hestrova.example
Thank you for taking the time to consider designing a website for us. We are web developers based in Stockton, CA, USA. Most of our projects go through the same process. Understanding this process may help you win a project with us. We custom-code all of our websites in-house. We don’t have any requirements as to what tools you use for your design, but we prefer Figma files. For any design that we label as four-stars, we send it to the client for review. The client picks the final design they want us to use. Once we complete this process, we will continue to show additional clients all the four-star sites and purchase them later. Your designs will have multiple chances to sell. For better chances of success, we ask that you follow these guidelines.
IMAGES:
If you use any images or icons in the design, we ask that you have a link to the asset so we can purchase the image/icon. Most of the designs we submit do not have the customer’s images on them unless they have some great images. Be creative; show us the feeling you are trying to portray with your image choices. Use any royalty-free site you choose. We subscribe to Quenlix and mainly use their images, but we can purchase images outside of Quenlix.
PLEASE NOTE: we will not submit designs to clients with watermarks on the images.
FONTS:
We ask that you identify the fonts used in the design. This can be done in a message if you want. We typically use Google Fonts and Quenlix Fonts.
CONTENT:
We're always open to different content and ideas. We often submit designs with stock images so the client can see our vision. We typically take pictures after the website launch to use their images with our vision. Lorem Ipsum is fine for paragraphs, but we ask that you write the headers in correct English. We want to be able to show the vision and identify the sections of the website.
INSPIRATION:
We typically add a couple of links in the brief of websites we like to help you get started in your design.
REVISIONS:
We do not often ask for revisions of the designs unless we see something in the design that may not appeal to the client. If there are slight changes that we want to make, we do that in the development process.
FEEDBACK:
We rarely give feedback on designs during the design process. We are working on many website projects and do not have the time to provide feedback. We usually respond if your request is well thought out and asks specific questions, but a note asking “feedback, please” usually goes unanswered.

```html
<!DOCTYPE html>
<html lang="en">
<head>
<meta charset="utf-8">
<title>BrivoNeté — Water Delivery</title>
<link rel="stylesheet" href="https://fonts.googleapis.com/css2?family=Kumbh+Sans:wght@400;500;600;700&family=Poppins:wght@400;500;600;700&display=swap">
<style>
:root{
  --navy:#2b3478;
  --navy-deep:#222a66;
  --blue:#1fa9e4;
  --blue-soft:#cfeaf8;
  --ice:#eef8fd;
  --ink:#1f2540;
  --grey:#6b7085;
  --white:#ffffff;
}
*{margin:0;padding:0;box-sizing:border-box}
html,body{width:1200px;height:4563px;overflow:hidden}
body{position:relative;background:var(--white);font-family:"Poppins",sans-serif;color:var(--ink)}
.abs{position:absolute}
.heading{font-family:"Kumbh Sans",sans-serif;font-weight:500;color:var(--ink)}
.accent{color:var(--blue)}
.photo{position:absolute;border-radius:50%}
.btn{position:absolute;background:var(--blue);color:var(--white);border-radius:30px;font-weight:600;font-size:13px;display:flex;align-items:center;justify-content:center;text-transform:uppercase}
.text-link{position:absolute;left:0;width:1200px;text-align:center;font-size:13px;font-weight:600;color:var(--blue);text-transform:uppercase}
.text-link span{border-bottom:1.5px solid var(--blue);padding-bottom:2px}

/* header */
.topbar{left:632px;top:0;width:568px;height:32px;background:var(--blue);border-bottom-left-radius:18px;color:var(--white);font-size:12px;display:flex;align-items:center;gap:28px;padding-left:44px}
.topbar .sep{width:1px;height:14px;background:rgba(255,255,255,.7)}
.brand{display:flex;align-items:center;gap:10px}
.brand-dot{width:34px;height:34px;border-radius:50%;background:var(--blue)}
.brand-name{font-family:"Kumbh Sans",sans-serif;font-weight:600;font-size:40px;color:var(--blue);line-height:1}
.nav{left:459px;top:56px;display:flex;gap:0;font-size:13px;font-weight:500;color:var(--ink)}
.nav a{position:absolute;white-space:nowrap;text-decoration:none;color:var(--ink)}
.nav a.active{color:var(--blue)}

/* hero */
.hero-title{left:85px;top:322px;font-size:42px;line-height:1.22;color:var(--white);font-weight:500}
.hero-copy{left:87px;top:441px;width:470px;font-size:14px;line-height:1.6;color:var(--white);font-weight:500}

/* features */
.section-title{left:0;width:1200px;text-align:center;font-size:32px}
.feature{position:absolute;top:907px;width:232px;height:236px;border:2px dashed var(--navy);border-radius:20px;background:var(--white);text-align:center;padding-top:30px}
.feature.featured{border:2px solid var(--blue)}
.feature h3{font-family:"Kumbh Sans",sans-serif;font-weight:500;font-size:16px;margin-top:14px;color:var(--ink)}
.feature.featured h3{color:var(--blue)}
.feature p{font-size:12px;line-height:1.5;color:var(--grey);margin:6px 22px 0}

/* about */
.about-title{left:647px;top:1412px;font-size:32px}
.about-copy{left:649px;top:1468px;width:424px;font-size:13px;line-height:1.65;color:var(--grey)}

/* solutions */
.sol-card{position:absolute;top:1982px;height:349px;border-radius:18px;background:linear-gradient(180deg,#b9c3cc 0%,#8fb6cf 50%,#1fa9e4 100%)}
.sol-card.wide{left:188px;width:420px}
.sol-card .label{position:absolute;color:var(--white);font-family:"Kumbh Sans",sans-serif;font-weight:500;font-size:21px}
.sol-card .vertical{left:22px;bottom:30px;transform:rotate(-90deg);transform-origin:left bottom;line-height:1.1;white-space:nowrap;translate:26px 0}
.sol-card p{position:absolute;left:35px;top:278px;width:340px;font-size:12px;line-height:1.5;color:var(--white)}

/* sustainability */
.eco-title{left:154px;top:2570px;font-size:34px;line-height:1.2;color:var(--white)}
.eco-copy{left:155px;top:2660px;width:440px;font-size:13px;line-height:1.65;color:var(--white)}
.eco-card{position:absolute;left:650px;width:385px;height:92px;background:var(--white);border-radius:14px;border:2px dashed var(--navy);display:flex;align-items:center;padding-left:30px;gap:24px}
.eco-card.featured{border:2px solid var(--blue)}
.eco-card h4{font-family:"Kumbh Sans",sans-serif;font-weight:500;font-size:15px;color:var(--ink)}
.eco-card.featured h4{color:var(--blue)}
.eco-card p{font-size:11.5px;color:var(--grey);margin-top:4px}

/* management */
.manage-card{position:absolute;top:3061px;width:233px;height:234px;border-radius:18px;color:var(--white);text-align:center;padding-top:40px}
.manage-card h4{font-family:"Kumbh Sans",sans-serif;font-weight:500;font-size:15px;margin-top:16px}
.manage-card p{font-size:12px;margin-top:6px}
.manage-title{left:736px;top:3140px;font-size:34px;line-height:1.17}

/* testimonials */
.review{position:absolute;top:3447px;width:273px}
.avatar{width:72px;height:72px;border-radius:50%;margin-left:0}
.review p{font-size:12.5px;line-height:1.75;color:var(--grey);margin-top:32px}
.review .foot{border-top:1px solid #dfe2ea;margin-top:20px;padding-top:16px;display:flex;justify-content:space-between;font-size:13px;font-weight:600;color:var(--ink)}
.stars{color:#f6b418;letter-spacing:1px;font-size:12px}
.quote-mark{position:absolute;right:40px;top:58px;font-family:"Kumbh Sans",sans-serif;font-size:90px;line-height:1;color:var(--blue-soft);font-weight:700}
.dot{position:absolute;top:3714px;width:10px;height:10px;border-radius:50%;background:#c7cbd6}

/* contact */
.contact{left:230px;top:3784px;width:731px;height:360px;background:var(--blue);border-radius:26px;color:var(--white)}
.contact h2{position:absolute;left:58px;top:44px;font-family:"Kumbh Sans",sans-serif;font-weight:500;font-size:32px}
.contact .intro{position:absolute;left:58px;top:100px;width:300px;font-size:12px;line-height:1.6}
.contact-row{position:absolute;left:58px;display:flex;align-items:center;gap:14px}
.contact-row .ico{width:46px;height:46px;border-radius:8px;background:var(--navy);display:flex;align-items:center;justify-content:center}
.contact-row small{display:block;font-size:12px}
.contact-row strong{display:block;font-size:19px;font-weight:500}

/* footer */
.footer-links{left:0;top:4358px;width:1200px;display:flex;justify-content:center;gap:26px;color:var(--white);font-size:16px;font-weight:500}
.footer-links .bar{color:var(--blue)}
.social{position:absolute;top:4419px;width:42px;height:42px;border-radius:50%;background:var(--blue)}
.copyright{left:0;top:4529px;width:1200px;text-align:center;color:var(--white);font-size:12px}
</style>
</head>
<body>

<!-- ===== Hero background & waves ===== -->
<svg class="abs" style="left:0;top:0" width="1200" height="1000" viewBox="0 0 1200 1000">
  <rect x="0" y="97" width="1200" height="860" fill="#2b3478"/>
  <path d="M0 925 C120 860 260 820 420 790 C560 760 600 690 700 690 C820 690 860 770 980 770 C1080 770 1150 760 1200 740 L1200 1000 L0 1000 Z" fill="#1fa9e4" opacity=".25"/>
  <path d="M0 930 C120 870 270 840 420 800 C560 765 600 700 705 700 C830 700 860 780 985 780 C1090 780 1150 770 1200 755 L1200 1000 L0 1000 Z" fill="#ffffff"/>
</svg>

<!-- ===== Header ===== -->
<div class="abs" style="left:0;top:0;width:1200px;height:97px;background:var(--white)"></div>
<div class="abs topbar">
  <span>&#9993;&nbsp; Email: support@brivonete.example</span>
  <span class="sep"></span>
  <span>
    <svg width="12" height="12" viewBox="0 0 24 24" style="vertical-align:-1px"><path d="M6.6 10.8a15 15 0 0 0 6.6 6.6l2.2-2.2a1 1 0 0 1 1-.25 11.4 11.4 0 0 0 3.6.57 1 1 0 0 1 1 1V20a1 1 0 0 1-1 1A17 17 0 0 1 3 4a1 1 0 0 1 1-1h3.5a1 1 0 0 1 1 1c0 1.25.2 2.45.57 3.57a1 1 0 0 1-.25 1z" fill="#fff"/></svg>
    &nbsp;Phone: 1-800-XXX-XXXX</span>
</div>
<div class="abs brand" style="left:88px;top:28px">
  <span class="brand-dot"></span><span class="brand-name">BrivoNeté</span>
</div>
<nav class="abs nav">
  <a class="active" style="left:0">Home</a>
  <a style="left:64px">Water Products</a>
  <a style="left:183px">Solutions</a>
  <a style="left:266px">Resources</a>
  <a style="left:355px">Sustainability</a>
  <a style="left:464px">Support</a>
</nav>
<div class="btn" style="left:994px;top:48px;width:117px;height:35px"></div>

<!-- ===== Hero ===== -->
<h1 class="abs heading hero-title">Pure, <span class="accent">Refreshing Water</span><br>Delivered Your Way!</h1>
<p class="abs hero-copy">Experience the convenience of fresh, purified water delivered to your home, office, or business.</p>
<div class="btn" style="left:88px;top:505px;width:153px;height:50px"></div>
<svg class="abs" style="left:86px;top:645px" width="52" height="80" viewBox="0 0 52 80">
  <path d="M26 2 C26 2 2 34 2 52 A24 24 0 0 0 50 52 C50 34 26 2 26 2 Z" fill="#1fa9e4"/>
  <circle cx="26" cy="52" r="12" fill="#fff"/>
  <path d="M26 45 V58 M21 53 L26 58 L31 53" stroke="#1fa9e4" stroke-width="2.5" fill="none" stroke-linecap="round"/>
</svg>
<div class="photo" role="img" aria-label="Delivery worker carrying a large water bottle" style="left:704px;top:170px;width:120px;height:120px;background:linear-gradient(135deg,#dfe9f2,#3d8fd4);border:4px solid #fff"></div>
<div class="photo" role="img" aria-label="Family smiling and drinking water together in a kitchen" style="left:732px;top:242px;width:336px;height:336px;background:linear-gradient(135deg,#e8e2dc,#b9a596);border:3px solid #fff"></div>
<div class="photo" role="img" aria-label="Woman holding a glass of water" style="left:599px;top:461px;width:184px;height:184px;background:linear-gradient(135deg,#cfd4dc,#b38b78);border:4px solid #fff"></div>
<div class="photo" role="img" aria-label="Man pouring water into a glass" style="left:956px;top:463px;width:212px;height:212px;background:linear-gradient(135deg,#e9edf1,#8aa3b8);border:6px solid #fff"></div>

<!-- ===== Better Water, Guaranteed ===== -->
<div class="abs" style="left:899px;top:855px;width:116px;height:116px;border-radius:50%;background:var(--blue)"></div>
<h2 class="abs heading section-title" style="top:840px">Better Water, <span class="accent">Guaranteed</span></h2>
<div class="feature" style="left:234px">
  <svg width="90" height="84" viewBox="0 0 90 84"><path d="M45 6 C45 6 26 30 26 44 A19 19 0 0 0 64 44 C64 30 45 6 45 6Z" fill="none" stroke="#2b3478" stroke-width="3"/><path d="M52 22 C52 22 44 32 44 38 A8 8 0 0 0 60 38 C60 32 52 22 52 22Z" fill="#1fa9e4"/><ellipse cx="45" cy="66" rx="38" ry="11" fill="none" stroke="#2b3478" stroke-width="3"/></svg>
  <h3>100% Purity Tested</h3>
  <p>Every drop meets the highest safety standards.</p>
</div>
<div class="feature featured" style="left:484px">
  <svg width="90" height="84" viewBox="0 0 90 84"><rect x="12" y="10" width="66" height="36" rx="3" fill="none" stroke="#2b3478" stroke-width="3"/><path d="M22 20h46M22 28h46M22 36h30" stroke="#1fa9e4" stroke-width="3"/><path d="M40 46 V74 H60 L66 56 L54 52 V46" fill="#fff" stroke="#2b3478" stroke-width="3" stroke-linejoin="round"/></svg>
  <h3>Flexible Subscription</h3>
  <p>Modify, pause, or cancel anytime.</p>
</div>
<div class="feature" style="left:734px">
  <svg width="90" height="84" viewBox="0 0 90 84"><circle cx="50" cy="36" r="28" fill="none" stroke="#1fa9e4" stroke-width="3"/><text x="50" y="43" text-anchor="middle" font-family="Kumbh Sans,sans-serif" font-size="18" font-weight="600" fill="#2b3478">24/7</text><path d="M14 40 C10 56 24 74 40 78 L46 70 L36 62 L30 66 C24 60 22 54 22 48 L28 44 L22 34 Z" fill="#fff" stroke="#2b3478" stroke-width="3" stroke-linejoin="round"/></svg>
  <h3>24/7 Customer Support</h3>
  <p>Dedicated service whenever you need us.</p>
</div>
<div class="text-link" style="top:1173px"><span>Compare Subscription Plans</span></div>

<!-- ===== About ===== -->
<svg class="abs" style="left:0;top:1215px" width="1200" height="605" viewBox="0 0 1200 605">
  <defs><linearGradient id="aboutBg" x1="0" y1="0" x2="0" y2="1"><stop offset="0" stop-color="#e3f3fc"/><stop offset="1" stop-color="#f3fafe"/></linearGradient></defs>
  <path d="M0 160 C120 60 220 0 300 20 C420 60 520 150 700 130 C900 110 1000 20 1200 10 L1200 605 L0 605 Z" fill="url(#aboutBg)"/>
  <path d="M168 605 A183 183 0 0 1 533 605 Z" fill="#cfeaf8"/>
</svg>
<div class="photo" role="img" aria-label="Woman in a blue sweater holding a glass water bottle" style="left:131px;top:1319px;width:436px;height:436px;background:linear-gradient(135deg,#eef1f4,#a9b8c9);border:4px solid var(--blue)"></div>
<div class="photo" role="img" aria-label="Masked delivery worker holding a water jug" style="left:456px;top:1590px;width:134px;height:134px;background:linear-gradient(135deg,#d6e4f0,#3a78c2);border:5px solid #fff"></div>
<h2 class="abs heading about-title">About <span class="accent">BrivoNeté</span></h2>
<p class="abs about-copy">At BrivoNeté, we believe clean, refreshing water should be accessible to everyone, anytime, anywhere. That's why we've dedicated ourselves to delivering premium, purified water straight to your home, office, or business with convenience, reliability, and sustainability in mind. At BrivoNeté, we believe clean, refreshing water should be accessible to everyone, anytime, anywhere. That's why we've dedicated ourselves to delivering premium, purified water straight to your home, office, or business with convenience, reliability.</p>
<div class="btn" style="left:650px;top:1678px;width:144px;height:43px">Read More</div>

<!-- ===== Solutions ===== -->
<h2 class="abs heading section-title" style="top:1882px">Water <span class="accent">Delivery Solutions</span> for Every Need</h2>
<p class="abs" style="left:0;top:1937px;width:1200px;text-align:center;font-size:13px;color:var(--grey)">Whether you need fresh water at home, in the office, or on the go, BrivoNeté has the perfect solution.</p>
<div class="sol-card wide" role="img" aria-label="Family raising glasses of water at the kitchen table">
  <span class="label" style="left:35px;top:229px">For Your Home</span>
  <p>Enjoy crisp, clean water for drinking, cooking, and everyday hydration. Our BPA-free bottles ensure safety for your entire family.</p>
</div>
<div class="sol-card" role="img" aria-label="Woman drinking water at work" style="left:624px;width:124px"><span class="label vertical">For Your<br>Workplace</span></div>
<div class="sol-card" role="img" aria-label="Man drinking from a bottle after exercise" style="left:762px;width:124px"><span class="label vertical">For Active<br>Lifestyles</span></div>
<div class="sol-card" role="img" aria-label="Woman holding a glass of water in an office" style="left:900px;width:124px"><span class="label vertical">Custom<br>Business Solutions</span></div>
<div class="text-link" style="top:2361px"><span>View All Delivery Options</span></div>

<!-- ===== Sustainability ===== -->
<svg class="abs" style="left:0;top:2350px" width="1200" height="760" viewBox="0 0 1200 760">
  <path d="M0 160 C80 110 160 60 260 70 C380 80 420 140 560 130 C720 120 820 20 960 10 C1060 2 1140 20 1200 40 L1200 560 C1120 600 1020 580 900 560 C760 540 680 520 520 560 C360 600 300 680 180 700 C100 714 40 740 0 760 Z" fill="#2b3478"/>
  <path d="M0 200 C120 140 200 110 300 120 C420 130 460 190 600 175" fill="none" stroke="#3b4690" stroke-width="1" opacity=".6"/>
</svg>
<h2 class="abs heading eco-title"><span class="accent" style="font-weight:600">Sustainability</span><br>Starts with Every Drop</h2>
<p class="abs eco-copy">We believe every drop counts—not just for hydration, but for the planet. Our eco-friendly approach ensures <b>responsible sourcing</b>, <b>reduced plastic waste, and energy-efficient delivery.</b></p>
<div class="btn" style="left:156px;top:2744px;width:411px;height:45px">Learn More About Our Sustainability Efforts</div>
<div class="eco-card" style="top:2567px">
  <svg width="56" height="60" viewBox="0 0 56 60"><rect x="6" y="16" width="18" height="40" rx="5" fill="none" stroke="#2b3478" stroke-width="2.5"/><rect x="11" y="6" width="8" height="10" fill="none" stroke="#2b3478" stroke-width="2.5"/><rect x="30" y="28" width="20" height="28" rx="4" fill="none" stroke="#1fa9e4" stroke-width="2.5"/><path d="M36 22h8v6h-8z" fill="none" stroke="#1fa9e4" stroke-width="2.5"/></svg>
  <div><h4>Reusable Bottle Program</h4><p>Reduce single-use plastic waste.</p></div>
</div>
<div class="eco-card featured" style="top:2673px">
  <svg width="62" height="50" viewBox="0 0 62 50"><path d="M14 10h26v26H14zM40 18h10l8 10v8H40z" fill="none" stroke="#2b3478" stroke-width="2.5" stroke-linejoin="round"/><circle cx="22" cy="40" r="5" fill="#fff" stroke="#1fa9e4" stroke-width="2.5"/><circle cx="48" cy="40" r="5" fill="#fff" stroke="#1fa9e4" stroke-width="2.5"/><path d="M2 18h9M4 24h7M0 30h11" stroke="#1fa9e4" stroke-width="2.5"/></svg>
  <div><h4>Eco-Friendly Delivery Fleet</h4><p>Lower carbon footprint.</p></div>
</div>
<div class="eco-card" style="top:2777px">
  <svg width="60" height="54" viewBox="0 0 60 54"><text x="2" y="24" font-family="Kumbh Sans,sans-serif" font-size="24" font-weight="500" fill="none" stroke="#1fa9e4" stroke-width="1.2">BPA</text><text x="2" y="46" font-family="Kumbh Sans,sans-serif" font-size="16" fill="#1fa9e4">FREE</text><path d="M46 34 C50 38 56 36 56 30 C50 30 46 32 46 40" fill="none" stroke="#2b3478" stroke-width="2"/></svg>
  <div><h4>BPA-Free Packaging</h4><p>Safe for you and the environment.</p></div>
</div>

<!-- ===== Management ===== -->
<div class="abs" style="left:181px;top:3242px;width:92px;height:92px;border-radius:50%;background:var(--blue-soft)"></div>
<div class="manage-card" style="left:216px;background:var(--navy-deep)">
  <svg width="96" height="84" viewBox="0 0 96 84"><rect x="26" y="6" width="44" height="72" rx="3" fill="none" stroke="#fff" stroke-width="2.5"/><path d="M34 20h28M34 30h28M34 40h28M34 50h28M34 60h20" stroke="#fff" stroke-width="2.5"/><rect x="10" y="20" width="16" height="46" fill="none" stroke="#fff" stroke-width="2.5"/><rect x="70" y="20" width="16" height="46" fill="none" stroke="#fff" stroke-width="2.5"/></svg>
  <h4>Modify Subscriptions</h4><p>Change your plan anytime.</p>
</div>
<div class="manage-card" style="left:464px;background:var(--blue)">
  <svg width="96" height="84" viewBox="0 0 96 84"><circle cx="48" cy="42" r="36" fill="none" stroke="#fff" stroke-width="2.5" stroke-dasharray="6 3"/><circle cx="48" cy="42" r="24" fill="none" stroke="#fff" stroke-width="2.5"/><path d="M38 42l7 7 13-14" fill="none" stroke="#fff" stroke-width="3" stroke-linecap="round" stroke-linejoin="round"/></svg>
  <h4>Hassle-Free Reordering</h4><p>One-click refills available.</p>
</div>
<h2 class="abs heading manage-title">Effortless<br><span class="accent" style="font-weight:600">Management</span> at<br>Your Fingertips</h2>

<!-- ===== Testimonials ===== -->
<h2 class="abs heading section-title" style="top:3375px">What Our <span class="accent">Customers</span> Say</h2>
<div class="review" style="left:117px">
  <div class="avatar" role="img" aria-label="Customer portrait" style="background:linear-gradient(135deg,#f4b33d,#e08a2a)"></div>
  <span class="quote-mark">&ldquo;</span>
  <p>Since we partnered with HelmQuarry our application has never been faster. We no longer worry about traffic spikes or unexpected downtime.</p>
  <div class="foot"><span>Marlo Quentin</span><span class="stars">&#9733;&#9733;&#9733;&#9733;&#9733;</span></div>
</div>
<div class="review" style="left:463px">
  <div class="avatar" role="img" aria-label="Customer portrait" style="background:linear-gradient(135deg,#c9cde2,#7f86b3)"></div>
  <span class="quote-mark">&ldquo;</span>
  <p>Since we partnered with HelmQuarry our application has never been faster. We no longer worry about traffic spikes or unexpected downtime.</p>
  <div class="foot"><span>Marlo Quentin</span><span class="stars">&#9733;&#9733;&#9733;&#9733;&#9733;</span></div>
</div>
<div class="review" style="left:810px">
  <div class="avatar" role="img" aria-label="Customer portrait" style="background:linear-gradient(135deg,#f0745a,#d9432c)"></div>
  <span class="quote-mark">&ldquo;</span>
  <p>Since we partnered with HelmQuarry our application has never been faster. We no longer worry about traffic spikes or unexpected downtime.</p>
  <div class="foot"><span>Marlo Quentin</span><span class="stars">&#9733;&#9733;&#9733;&#9733;&#9733;</span></div>
</div>
<span class="dot" style="left:569px"></span>
<span class="dot" style="left:589px;background:var(--blue)"></span>
<span class="dot" style="left:609px"></span>

<!-- ===== Footer background ===== -->
<svg class="abs" style="left:0;top:3940px" width="1200" height="623" viewBox="0 0 1200 623">
  <path d="M0 200 C200 150 300 110 500 130 C700 150 800 60 960 30 C1080 8 1150 20 1200 30 L1200 623 L0 623 Z" fill="#2b3478"/>
</svg>

<!-- ===== Contact ===== -->
<div class="abs contact">
  <h2>Contact Us</h2>
  <p class="intro">It is a long established fact that a reader will be distracted by the readable content of a page when looking at its layout. The point of using Lorem Ipsum is that it</p>
  <div class="contact-row" style="top:196px">
    <span class="ico"><svg width="20" height="20" viewBox="0 0 24 24"><path d="M6.6 10.8a15 15 0 0 0 6.6 6.6l2.2-2.2a1 1 0 0 1 1-.25 11.4 11.4 0 0 0 3.6.57 1 1 0 0 1 1 1V20a1 1 0 0 1-1 1A17 17 0 0 1 3 4a1 1 0 0 1 1-1h3.5a1 1 0 0 1 1 1c0 1.25.2 2.45.57 3.57a1 1 0 0 1-.25 1z" fill="#fff"/></svg></span>
    <div><small>Call Us</small><strong>1-800-XXX-XXXX</strong></div>
  </div>
  <div class="contact-row" style="top:264px">
    <span class="ico"><svg width="18" height="22" viewBox="0 0 18 22"><path d="M9 1a8 8 0 0 0-8 8c0 6 8 12 8 12s8-6 8-12a8 8 0 0 0-8-8z" fill="#fff"/><circle cx="9" cy="9" r="3" fill="#2b3478"/></svg></span>
    <div><small>Email Address</small><strong>support@brivonete.example</strong></div>
  </div>
  <div class="abs" role="img" aria-label="Street map of the service area" style="left:407px;top:48px;width:276px;height:276px;border-radius:50%;background:linear-gradient(135deg,#eef0f2,#d8dde3);border:8px solid #8fd3f2"></div>
  <svg class="abs" style="left:525px;top:156px" width="42" height="42" viewBox="0 0 42 42"><circle cx="21" cy="21" r="21" fill="#2b3478"/><path d="M21 10a7 7 0 0 0-7 7c0 5 7 12 7 12s7-7 7-12a7 7 0 0 0-7-7z" fill="#fff"/><circle cx="21" cy="17" r="2.5" fill="#2b3478"/></svg>
</div>

<!-- ===== Footer ===== -->
<div class="abs brand" style="left:412px;top:4226px">
  <span class="brand-dot" style="width:50px;height:50px"></span><span class="brand-name" style="font-size:66px">BrivoNeté</span>
</div>
<div class="abs footer-links">
  <span>Home</span><span class="bar">|</span><span>About Us</span><span class="bar">|</span><span>FAQs</span><span class="bar">|</span><span>Sustainability</span><span class="bar">|</span><span>Customer Support</span><span class="bar">|</span><span>Social Media Links</span>
</div>
<span class="social" style="left:502px"></span>
<span class="social" style="left:553px"></span>
<span class="social" style="left:605px"></span>
<span class="social" style="left:656px"></span>
<div class="abs" style="left:74px;top:4511px;width:1052px;height:1px;background:rgba(255,255,255,.3)"></div>
<p class="abs copyright">© Copyright 2025, BrivoNeté Water delivery All Rights Reserved</p>
<svg class="abs" style="left:1124px;top:4481px" width="60" height="60" viewBox="0 0 60 60"><circle cx="30" cy="30" r="30" fill="#1fa9e4"/><path d="M22 34l8-8 8 8" fill="none" stroke="#fff" stroke-width="3" stroke-linecap="round" stroke-linejoin="round"/></svg>

</body>
</html>
```